Business Card Design

we are a brand new cable TV network devoted to self improvement and leading a better life called FLOURIVO TV.I have a logo. We have 3 executives that need cards.I want it to be a heavy stock card: professional but showing our creative nature

Industry/Entity Type

Business

Contact Information for Business Card

CLAUDIA SAENZ AMLIECEO350 San Juan DrPonte Vedra Beach FL 32082904-473-5953

```html
<!DOCTYPE html>
<html lang="en">
<head>
<meta charset="utf-8">
<title>FLOURIVO TV Business Card</title>
<link rel="stylesheet" href="https://fonts.googleapis.com/css2?family=Source+Sans+3:wght@400;600;700&display=swap">
<style>
  :root {
    --page-bg: #e9e9e9;
    --card-white: #ffffff;
    --brand-red: #b8232f;
    --ray-red: #c0303a;
    --ink: #1c1c1c;
  }
  * { margin: 0; padding: 0; box-sizing: border-box; }
  html, body {
    width: 1105px;
    height: 1200px;
    overflow: hidden;
    background: var(--page-bg);
    font-family: "Source Sans 3", "Myriad Pro", Arial, sans-serif;
  }
  .canvas {
    position: relative;
    width: 1105px;
    height: 1200px;
  }
  .business-card {
    position: absolute;
    left: 102px;
    top: 343px;
    width: 900px;
    height: 514px;
    overflow: hidden;
    background: var(--card-white);
  }
  .card-backdrop {
    position: absolute;
    inset: 0;
    background: radial-gradient(ellipse 62% 68% at 50% 50%,
      var(--card-white) 0%,
      var(--card-white) 38%,
      rgba(192, 48, 58, 0.35) 70%,
      var(--ray-red) 100%);
  }
  .card-content {
    position: absolute;
    inset: 0;
    text-align: center;
    color: var(--ink);
  }
  .brand-name {
    position: absolute;
    left: 0; right: 0;
    top: 130px;
    font-size: 64px;
    font-weight: 700;
    line-height: 1;
    letter-spacing: 1px;
    color: var(--brand-red);
  }
  .person-name {
    position: absolute;
    left: 0; right: 0;
    top: 231px;
    font-size: 30px;
    font-weight: 600;
    line-height: 1;
    color: var(--brand-red);
  }
  .person-title {
    position: absolute;
    left: 0; right: 0;
    top: 276px;
    font-size: 26px;
    font-weight: 400;
    line-height: 1;
  }
  .address {
    position: absolute;
    left: 0; right: 0;
    top: 318px;
    font-size: 24px;
    font-weight: 400;
    line-height: 31px;
    font-style: normal;
  }
  .phone {
    position: absolute;
    left: 0; right: 0;
    top: 388px;
    font-size: 24px;
    line-height: 1;
    display: flex;
    justify-content: center;
    align-items: center;
    gap: 8px;
  }
  .phone-icon { width: 22px; height: 22px; fill: var(--brand-red); }
</style>
</head>
<body>
<div class="canvas">
  <section class="business-card">
    <div class="card-backdrop" role="img" aria-label="Radiating red sunburst rays fading to a white centre"></div>
    <div class="card-content">
      <div class="brand-name">FLOURIVO TV</div>
      <div class="person-name">MIRELLA OKAFOR DUNST</div>
      <div class="person-title">CEO</div>
      <address class="address">718 Harlow Creek Dr<br>Ponte Vedra Beach FL 32097</address>
      <div class="phone">
        <svg class="phone-icon" viewBox="0 0 24 24" aria-hidden="true">
          <path d="M6.6 10.8c1.4 2.8 3.8 5.1 6.6 6.6l2.2-2.2c.3-.3.7-.4 1-.2 1.1.4 2.3.6 3.6.6.6 0 1 .4 1 1V20c0 .6-.4 1-1 1C10.6 21 3 13.4 3 4c0-.6.4-1 1-1h3.5c.6 0 1 .4 1 1 0 1.3.2 2.5.6 3.6.1.3 0 .7-.2 1L6.6 10.8z"/>
        </svg>
        <span>904-618-2047</span>
      </div>
    </div>
  </section>
</div>
</body>
</html>
```